Summer Resolution Do it Now

I run a hypnotherapy practice that helps people
Loose Weight,Stop smoking ,overcome fear of Public speaking and improve Confidence and positive attitude.
I like to market a especific group in the CBD Melbourne as I only practice once a week in the city.

I have some photographs that will go well for the flyer what I am after is something very professional ,sober and elegant.

Target Market(s)

CBD corporate Melbourne market 25 till 60 year old

Industry/Entity Type

Hypnotherapy

Requirements
Must have
• flyer should be two sided , must have http://www.calmtrancestudio.example/ and the phone number 0491627058 and encourage to book online .

```html
<!DOCTYPE html>
<html lang="en">
<head>
<meta charset="utf-8">
<title>Daniel Whitcombe – Melbourne Hypnotherapist</title>
<link rel="stylesheet" href="https://fonts.googleapis.com/css2?family=Arimo:wght@400;700&display=swap">
<style>
  :root{
    --brand-blue:#1a5aa6;
    --deep-blue:#0b2f66;
    --mid-blue:#1d56a8;
    --sky-blue:#4f9ae0;
    --accent-yellow:#f4e04d;
    --text-dark:#2b2b2b;
    --text-grey:#3d3d3d;
    --paper:#ffffff;
    --footer-light:#f2f2f2;
    --footer-dark:#b9bcc0;
    --photo-light:#f4f1ec;
    --photo-skin:#e4c2a6;
    --photo-green:#2f9a4a;
  }
  *{margin:0;padding:0;box-sizing:border-box}
  html,body{width:707px;height:1200px;overflow:hidden;background:var(--paper)}
  body{font-family:"Arimo",Arial,sans-serif}
  .flyer{position:relative;width:707px;height:1200px;overflow:hidden;background:var(--paper)}

  .hero-photo{position:absolute;left:0;top:0;width:707px;height:760px;
    background:
      radial-gradient(ellipse 230px 300px at 470px 330px,var(--photo-skin) 0%,rgba(228,194,166,.6) 55%,rgba(228,194,166,0) 100%),
      linear-gradient(180deg,rgba(255,255,255,0) 55%,var(--photo-green) 80%),
      linear-gradient(135deg,var(--paper) 0%,var(--photo-light) 45%,#d9d2c6 100%);}

  .brand{position:absolute;left:18px;top:16px;display:flex;align-items:center;gap:12px}
  .brand-mark{width:74px;height:74px;border-radius:50%;background:var(--brand-blue)}
  .brand-name{color:var(--brand-blue);font-size:23px;font-weight:700;line-height:27px}
  .brand-url{color:var(--brand-blue);font-size:10px;font-weight:700;line-height:14px}

  .intro{position:absolute;left:28px;top:160px;width:228px;height:480px;
    background:rgba(255,255,255,.72);padding:14px 6px;
    text-align:center;color:var(--text-dark);font-size:14.5px;font-weight:700;line-height:21px}

  .band{position:absolute;left:0;top:600px;width:707px;height:600px}

  .treat{position:absolute;left:0;top:752px;width:707px}
  .treat-title{color:var(--accent-yellow);font-size:27px;font-weight:700;text-align:center}
  .treat-list{list-style:none;display:grid;grid-template-columns:232px 380px;
    column-gap:0;margin:14px 0 0 35px;color:var(--paper);font-size:17px;font-weight:700;line-height:24px}
  .treat-list li{display:flex;align-items:center;gap:9px}
  .treat-list li::before{content:"";width:11px;height:11px;background:var(--accent-yellow);flex:none}
  .treat-more{margin-top:10px;color:var(--accent-yellow);font-size:40px;font-weight:700;text-align:center}

  .booking{position:absolute;left:0;top:996px;width:707px;text-align:center;
    color:var(--text-grey);font-size:15.5px;line-height:21px}
  .contact{position:absolute;left:66px;display:flex;align-items:center;gap:16px;
    color:var(--text-grey);font-size:28px}
  .contact svg{flex:none}
  .contact-web{top:1090px}
  .contact-phone{top:1138px}
</style>
</head>
<body>
<main class="flyer">
  <div class="hero-photo" role="img" aria-label="Smiling professional woman with blonde hair and glasses on her head, wearing a green top, against a light background"></div>

  <header class="brand">
    <div class="brand-mark"></div>
    <div>
      <div class="brand-name">Daniel Whitcombe<br>Melbourne Hypnotherapist</div>
      <div class="brand-url">www.CalmTranceStudio.example</div>
    </div>
  </header>

  <section class="intro">
    Hypnotherapy is a powerful tool<br>and can assist you<br>in making desired changes to<br>your life such as helping<br>you quit smoking,<br>lose weight or to improve<br>public speaking among<br>many other things.<br>Daniel Whitcombe is a<br>Clinical Hypnotherapist<br>based in<br>Melbourne's CBD and<br>Western Suburbs (Footscray).<br>People from all over Australia<br>come to see<br>Daniel for<br>hypnotherapy consultations.
  </section>

  <svg class="band" viewBox="0 0 707 600" aria-hidden="true">
    <defs>
      <linearGradient id="bandFill" x1="0" y1="0" x2="0" y2="1">
        <stop offset="0" stop-color="#2d6ec2"/>
        <stop offset=".45" stop-color="#164a96"/>
        <stop offset="1" stop-color="#0b2f66"/>
      </linearGradient>
      <linearGradient id="footerFill" x1="0" y1="0" x2="0" y2="1">
        <stop offset="0" stop-color="#f4f4f4"/>
        <stop offset=".6" stop-color="#dcdde0"/>
        <stop offset="1" stop-color="#b9bcc0"/>
      </linearGradient>
    </defs>
    <rect x="0" y="0" width="707" height="600" fill="url(#footerFill)"/>
    <path d="M0 70 C220 40 470 10 707 30 L707 320 C470 290 220 330 0 380 Z" fill="url(#bandFill)"/>
    <path d="M0 70 C220 40 470 10 707 30" fill="none" stroke="#6fb3ec" stroke-width="4"/>
    <path d="M0 58 C240 20 480 0 707 14" fill="none" stroke="#9fd0f5" stroke-width="2" opacity=".8"/>
    <path d="M0 380 C220 330 470 290 707 320" fill="none" stroke="#4f9ae0" stroke-width="5"/>
    <path d="M0 395 C240 345 480 308 707 336" fill="none" stroke="#9fb8d6" stroke-width="2" opacity=".7"/>
  </svg>

  <section class="treat">
    <h2 class="treat-title">Hypnosis has been used to treat:</h2>
    <ul class="treat-list">
      <li>Stopping Smoking</li><li>Public Speaking Fears</li>
      <li>Alcohol Moderation</li><li>Bruxism / Teeth Grinding / Teeth Clenching</li>
      <li>Losing Weight</li><li>IBS</li>
    </ul>
    <p class="treat-more">And Much More</p>
  </section>

  <p class="booking">You can book an appointment online to see<br>Daniel via the booking system which can be accessed below.<br>Alternatively, you can call to enquire or to book an appointment.</p>

  <div class="contact contact-web">
    <svg width="30" height="30" viewBox="0 0 30 30" aria-hidden="true">
      <circle cx="15" cy="15" r="13" fill="#e0b11a"/>
      <g fill="none" stroke="#7a5a00" stroke-width="1.5">
        <circle cx="15" cy="15" r="13"/><ellipse cx="15" cy="15" rx="6" ry="13"/>
        <line x1="2" y1="15" x2="28" y2="15"/><line x1="4" y1="8" x2="26" y2="8"/><line x1="4" y1="22" x2="26" y2="22"/>
      </g>
    </svg>
    <span>www.calmtrancestudio.example</span>
  </div>
  <div class="contact contact-phone">
    <svg width="30" height="26" viewBox="0 0 30 26" aria-hidden="true">
      <path d="M2 9 C2 3 28 3 28 9 L24 12 L21 9 L21 7 C17 6 13 6 9 7 L9 9 L6 12 Z" fill="#e0b11a"/>
      <path d="M7 13 L11 10 L19 10 L23 13 L25 24 L5 24 Z" fill="#e0b11a"/>
      <circle cx="15" cy="17" r="3.5" fill="#7a5a00"/>
    </svg>
    <span>0491627058</span>
  </div>
</main>
</body>
</html>
```